Charitable and Benefit Event Auctioneer and Emcee

My name is Wes
People know me as Wes The Auctioneer
My email is westheauctioneer@...
Include Phone number
This is a very unique and distinct type of Auctioneering that focuses on high profile charitable events including black tie galas, fundraisers and golf tournaments...
Clients include hospitals, schools, service agencies, corporations, foundations
Event consultation is also offered
Graduate of The Brightwater Valley School of Auctioneering
in the Fundraising Auction business since 1998

Reason: I have been too busy to give time to appropriate time to the designs submitted and I'm still having learning challenges with the pixelguild website.

Target Market(s)

Very high profile nonprofit organizations hosting gala events raising millions of dollars.

Industry/Entity Type

Events

Font styles to use
Sans Serif

Colors

Designer to choose colors to be used in the design.

Requirements
Must have
• Classy, eye catching, unique.

```html
<!DOCTYPE html>
<html lang="en">
<head>
<meta charset="utf-8">
<title>Wes The Auctioneer – Business Card</title>
<link href="https://fonts.googleapis.com/css2?family=Oswald:wght@400;600&display=swap" rel="stylesheet">
<style>
  :root {
    --page-bg: #e4e4e4;
    --card-black: #1c1c1d;
    --pattern-dark: #2a2a2b;
    --pattern-light: #6a6a6b;
    --accent-yellow: #f5e31b;
    --text-white: #f2f2f2;
  }
  * { margin: 0; padding: 0; box-sizing: border-box; }
  html, body {
    width: 1200px;
    height: 1000px;
    overflow: hidden;
    background: var(--page-bg);
  }
  .canvas {
    position: relative;
    width: 1200px;
    height: 1000px;
  }
  .card {
    position: absolute;
    left: 250px;
    width: 700px;
    height: 400px;
    border-radius: 22px;
    background: var(--card-black);
    overflow: hidden;
    box-shadow: 0 10px 30px rgba(0,0,0,0.18);
  }
  .card--front { top: 70px; }
  .card--back  { top: 530px; }

  .card__pattern {
    position: absolute;
    top: 0;
    right: 0;
    width: 74%;
    height: 100%;
    background: radial-gradient(ellipse at 58% 45%, var(--pattern-light) 0%, #4a4a4b 35%, var(--pattern-dark) 80%);
    clip-path: polygon(30% 0, 100% 0, 100% 100%, 70% 100%, 58% 62%, 44% 30%);
  }
  .card--back .card__pattern {
    clip-path: polygon(18% 0, 100% 0, 100% 100%, 66% 100%, 56% 64%, 40% 36%);
  }

  .card__content {
    position: absolute;
    left: 52px;
    bottom: 48px;
  }
  .card__title {
    font-family: "Oswald", sans-serif;
    font-weight: 600;
    font-size: 44px;
    letter-spacing: 1px;
    text-transform: uppercase;
    color: var(--accent-yellow);
  }
  .card__name {
    font-family: "Oswald", sans-serif;
    font-weight: 600;
    font-size: 56px;
    line-height: 1;
    text-transform: uppercase;
    color: var(--accent-yellow);
    margin-bottom: 12px;
  }
  .card__tagline {
    font-family: "Oswald", sans-serif;
    font-weight: 400;
    font-size: 17px;
    letter-spacing: 0.5px;
    text-transform: uppercase;
    color: var(--text-white);
  }
  .card__contact {
    font-family: "Oswald", sans-serif;
    font-weight: 400;
    font-size: 28px;
    line-height: 1.35;
    text-transform: uppercase;
    color: var(--text-white);
    margin-top: 8px;
  }
</style>
</head>
<body>
<main class="canvas">
  <section class="card card--front">
    <div class="card__pattern" role="img" aria-label="Checkered diamond pattern fading into a soft grey glow"></div>
    <div class="card__content">
      <p class="card__title">Wes The Auctioneer</p>
    </div>
  </section>

  <section class="card card--back">
    <div class="card__pattern" role="img" aria-label="Checkered diamond pattern fading into a soft grey glow"></div>
    <div class="card__content">
      <p class="card__name">Wes</p>
      <p class="card__tagline">Charitable and Benefit Event Auctioneer and Emcee</p>
      <p class="card__contact">555-201-4477<br>westheauctioneer@brightmail.ca</p>
    </div>
  </section>
</main>
</body>
</html>
```